simple, clean, smart design for PPT template!

We need a template design for ouw company Brenthollow. Please refer to the business cad design and our web site.

Our message is Wisdome and Knowledge, and the image is "simple" and "clean".
http://www.brenthollow.example/

You may want to refer to the company like KDT, Solvarine, RMN, Tyvor, etc.

Target Market(s)

Every business industry.

Industry/Entity Type

Consulting

Font styles to use
Other font styles liked:
• Please refer to your sense from our corporate image.

Requirements
Must have
• company logo. the colors should be limited to ones used for the logo. The final version of your file must be submitted in PPT format.
Nice to have
• The corporate image is always "simple and clean".
Should not have
• No pictures of human face.

```html
<!DOCTYPE html>
<html lang="en">
<head>
<meta charset="utf-8">
<title>Brenthollow presentation template</title>
<link rel="stylesheet" href="https://fonts.googleapis.com/css2?family=Open+Sans:ital,wght@0,400;0,600;0,700;1,400;1,600;1,700&display=swap">
<style>
:root{
  --stage:#8c8c8c;
  --paper:#ffffff;
  --green:#8dcf4f;
  --green-deep:#7cbd3e;
  --ink:#3c3c3c;
  --ink-soft:#555555;
  --bar:#2b2b2b;
  --bar-edge:#1a1a1a;
  --photo:#b9b9b9;
  --photo-dark:#8e8e8e;
  --rule:#d9d9d9;
}
*{box-sizing:border-box;margin:0;padding:0}
html,body{width:1200px;height:891px;overflow:hidden}
body{background:var(--stage);font-family:"Open Sans",Arial,sans-serif;color:var(--ink);position:relative}
.slide{position:absolute;background:var(--paper);overflow:hidden;box-shadow:0 4px 10px rgba(0,0,0,.35)}
.slide--cover{left:37px;top:27px;width:511px;height:381px}
.slide--services{left:614px;top:30px;width:512px;height:382px}
.slide--feature{left:40px;top:432px;width:504px;height:376px}
.slide--team{left:616px;top:434px;width:514px;height:386px}

.slide__footer{position:absolute;left:0;right:0;bottom:0;height:28px}
.slide__footer::before{content:"";position:absolute;left:0;right:0;top:0;height:7px;background:var(--green)}
.footer__bar{position:absolute;left:0;right:0;bottom:0;height:21px;background:linear-gradient(var(--bar),var(--bar-edge));display:flex;align-items:center;padding:0 18px 0 6px;color:#e8e8e8;font-size:7.5px}
.footer__nav{display:flex;gap:6px;margin-right:12px}
.footer__nav span{width:9px;height:7px;background:#555;border-radius:1px}
.footer__copy{margin-left:auto}
.wordmark{display:flex;align-items:center;gap:5px;font-weight:600;color:var(--green)}
.wordmark__dot{border-radius:50%;border:2px solid currentColor;flex:none}
.footer__bar .wordmark{color:#f2f2f2;font-size:11px}
.footer__bar .wordmark__dot{width:11px;height:11px}

.slide__title{position:absolute;font-size:12px;font-weight:700;color:var(--ink)}
.slide__subtitle{position:absolute;font-size:11px;color:var(--green)}

/* cover */
.cover__logo{position:absolute;left:41px;top:44px;font-size:25px}
.cover__logo .wordmark__dot{width:28px;height:28px;border-width:3px}
.cover__slogan{position:absolute;left:43px;top:92px;font-size:19.5px;font-weight:700;line-height:27.5px;color:var(--ink-soft)}
.cover__slogan em{color:var(--green);font-style:italic}
.cover__lede{position:absolute;left:45px;top:232px;width:175px;font-size:7.3px;line-height:10px;color:#333}

/* services */
.slide--services .slide__title{left:18px;top:21px}
.slide--services .slide__subtitle{left:18px;top:37px}
.services{position:absolute;left:15px;top:74px;display:flex}
.service{width:82px;padding:0 4px;border-right:1px solid var(--rule);min-height:246px}
.service:last-child{border-right:none}
.service__icon{width:34px;height:34px;border-radius:50%;background:var(--green);display:flex;align-items:center;justify-content:center;margin-bottom:9px}
.service__icon--dark{background:#3a3a3a}
.service__name{font-size:6.4px;font-weight:700;font-style:italic;color:#222;margin-bottom:4px}
.service__text{font-size:5.4px;line-height:7.7px;color:#333}

/* feature */
.feature__panel{position:absolute;left:0;top:0;width:100%;height:226px;background:var(--green)}
.slide--feature .slide__title{left:18px;top:20px}
.slide--feature .slide__subtitle{left:18px;top:36px;color:#fff}
.points{position:absolute;left:29px;top:107px;display:flex;gap:19px}
.point{width:128px;color:#fff}
.point__head{display:flex;align-items:center;gap:5px;font-size:11px;font-weight:700;margin-bottom:4px}
.point__text{font-size:8.3px;line-height:12px}
.testimonial{position:absolute;left:0;right:0;top:243px;text-align:center;font-style:italic}
.testimonial__title{font-size:11px;color:#222;margin-bottom:8px}
.testimonial__quote{font-size:8.3px;line-height:12px;color:#222;width:410px;margin:0 auto}
.testimonial__name{font-size:8.3px;font-weight:700;color:var(--green);margin-top:2px}

/* team */
.slide--team .slide__title{left:18px;top:21px}
.slide--team .slide__subtitle{left:18px;top:37px}
.team__band{position:absolute;left:0;top:106px}
.team__logo{position:absolute;left:12px;top:166px;font-size:25px;color:#fff}
.team__logo .wordmark__dot{width:26px;height:26px;border-width:3px}
.member{position:absolute;top:206px;color:#fff;font-size:9px;line-height:12px}
.member__name{display:block}
.member__role{font-size:7.2px;line-height:10px}
.member--a{left:161px}
.member--b{left:275px}
.member--c{left:387px}
</style>
</head>
<body>

<section class="slide slide--cover">
  <div class="wordmark cover__logo"><span class="wordmark__dot"></span>brenthollow</div>
  <h1 class="cover__slogan">Add your<br><em>presentation<br>Slogan</em> here and<br>some Powerful<br>things here</h1>
  <p class="cover__lede">What we need is a template (or master) which can be varied by ourselves from case to case. Most of our cases are colorful and it's important to transport the passion of</p>
  <footer class="slide__footer"><div class="footer__bar">
    <div class="footer__nav"><span></span><span></span><span></span></div>
    <span>www.brenthollow.example</span>
    <span class="footer__copy">© Copy right to brenthollow wisdom &amp; knowledge</span>
  </div></footer>
</section>

<section class="slide slide--services">
  <h2 class="slide__title">Our Services we do</h2>
  <p class="slide__subtitle">Your sub title here</p>
  <div class="services">
    <article class="service">
      <div class="service__icon"><svg width="16" height="18" viewBox="0 0 16 18"><rect x="1" y="1" width="14" height="16" rx="2" fill="none" stroke="#fff" stroke-width="1.6"/><rect x="4" y="4" width="8" height="3" fill="#fff"/><g fill="#fff"><rect x="4" y="9" width="2" height="2"/><rect x="7" y="9" width="2" height="2"/><rect x="10" y="9" width="2" height="2"/><rect x="4" y="12" width="2" height="2"/><rect x="7" y="12" width="2" height="2"/><rect x="10" y="12" width="2" height="2"/></g></svg></div>
      <h3 class="service__name">Finance &amp; Accounting</h3>
      <p class="service__text">Our Record-to-Report process services help you meet your goals, by streamlining and consolidating their operations. By utilizing a proven methodology we are able to reduce errors, increase response time and quickly adapt to changing business needs. We provide financial report under JGAAP/IFRS/USGAAP.<br>General Accounting<br>Account Reconciliation<br>Fixed Assets<br>Inventory and Revenue Accounting<br>Cost Accounting<br>Taxation<br>Compliance<br>Reporting<br>Internal Control and Audit Support</p>
    </article>
    <article class="service">
      <div class="service__icon service__icon--dark"><svg width="18" height="18" viewBox="0 0 18 18" fill="#fff"><circle cx="9" cy="4" r="2.5"/><circle cx="4" cy="13" r="2.5"/><circle cx="14" cy="13" r="2.5"/><path d="M9 7v3M6 11l3-1 3 1" stroke="#fff" stroke-width="1.2" fill="none"/></svg></div>
      <h3 class="service__name">HR &amp; Payroll</h3>
      <p class="service__text">Look to us for corporate legal support for every stage of your business, including incorporation services, preparation of shareholder meeting minutes and drafting of foreign language contracts. We also provide advisory and document preparation services when you need visas to bring overseas staff to Japan.<br>Company Registration/Dissolution<br>Business Compliance<br>Corporate Changes &amp; Filings<br>Corporate Minutes for Local Board Meeting<br>Work Visa</p>
    </article>
    <article class="service">
      <div class="service__icon"><svg width="14" height="18" viewBox="0 0 14 18"><rect x="1" y="2" width="12" height="15" rx="1" fill="none" stroke="#fff" stroke-width="1.5"/><rect x="4" y="0.5" width="6" height="3" fill="#fff"/><path d="M3.5 7h7M3.5 10h7M3.5 13h5" stroke="#fff" stroke-width="1.2"/></svg></div>
      <h3 class="service__name">Corporate Secretary</h3>
      <p class="service__text">Look to us for corporate legal support for every stage of your business, including incorporation services, preparation of shareholder meeting minutes and drafting of foreign language contracts. We also provide advisory and document preparation services when you need visas to bring overseas staff to Japan.<br>Company Registration/Dissolution<br>Business Compliance<br>Corporate Changes &amp; Filings<br>Corporate Minutes for Local Board Meeting<br>Work Visa</p>
    </article>
    <article class="service">
      <div class="service__icon service__icon--dark"><svg width="18" height="16" viewBox="0 0 18 16"><rect x="1" y="1" width="16" height="11" rx="1" fill="none" stroke="#fff" stroke-width="1.5"/><circle cx="9" cy="5" r="2" fill="#fff"/><path d="M5.5 11c0-2 7-2 7 0" fill="#fff"/><path d="M6 15h6" stroke="#fff" stroke-width="1.5"/></svg></div>
      <h3 class="service__name">IT Support</h3>
      <p class="service__text">We deliver timely on-site support for all your IT needs, from setup to operation and maintenance, and we can also coordinate your PMO for Corevant, Dataquill or other ERP implementation projects. Our bilingual project members will work closely with your home office team to provide vital local assistance.<br>Set-up Infrastructure Integration<br>Life Cycle Management<br>On-site Support<br>ERP/System Implementation<br>Web Site Localization</p>
    </article>
    <article class="service">
      <div class="service__icon"><svg width="18" height="16" viewBox="0 0 18 16" fill="#fff"><rect x="1" y="1" width="9" height="6" rx="1"/><path d="M3 7v3l3-3z"/><rect x="8" y="8" width="9" height="6" rx="1"/><path d="M15 14v2l-3-2z"/></svg></div>
      <h3 class="service__name">Interpreting</h3>
      <p class="service__text">If you need English or other foreign language support, we can also arrange interpreting for your business meetings, whether it's accompaniment for visiting executives or simultaneous or consecutive interpreting for meetings and events.<br>Escort Interpreting<br>Event/Presentation Interpreting<br>Japanese, Korean, Chinese, French, etc.</p>
    </article>
    <article class="service">
      <div class="service__icon service__icon--dark"><svg width="14" height="18" viewBox="0 0 14 18" fill="#fff"><circle cx="7" cy="4" r="3"/><path d="M2 17c0-6 2-9 5-9s5 3 5 9z"/></svg></div>
      <h3 class="service__name">Corporate Concierge</h3>
      <p class="service__text">Ask us for the detailed information you need to run your business in Japan, including transportation and conference room arrangement and even appropriate restaurants for business meals.<br>Business Trip Coordination<br>Booking Meeting/Banquet Room<br>Living Support for Expats<br>Various Daily Business Support</p>
    </article>
  </div>
  <footer class="slide__footer"><div class="footer__bar">
    <div class="footer__nav"><span></span><span></span><span></span></div>
    <div class="wordmark"><span class="wordmark__dot"></span>brenthollow</div>
    <span class="footer__copy">© Copy right to brenthollow wisdom &amp; knowledge</span>
  </div></footer>
</section>

<section class="slide slide--feature">
  <div class="feature__panel"></div>
  <h2 class="slide__title">Insert your Sub heading here</h2>
  <p class="slide__subtitle">Your sub title here</p>
  <div class="points">
    <article class="point">
      <h3 class="point__head"><svg width="26" height="22" viewBox="0 0 26 22"><path d="M1 1h24v15H9l-5 5v-5H1z" fill="#fff"/><path d="M6 5l4 7M10 5l4 7M14 5l4 7" stroke="var(--green)" stroke-width="2"/></svg>Number one</h3>
      <p class="point__text">What we need is a template (or master) which can be varied by ourselves from case to case. Most of our cases are colorful and it's important to transport the passion of</p>
    </article>
    <article class="point">
      <h3 class="point__head"><svg width="26" height="22" viewBox="0 0 26 22"><path d="M1 1h24v15H9l-5 5v-5H1z" fill="#fff"/><circle cx="10" cy="6" r="2.5" fill="var(--green)"/><circle cx="16" cy="6" r="2.5" fill="var(--green)"/><path d="M6 13c0-3 8-3 8 0zM12 13c0-3 8-3 8 0z" fill="var(--green)"/></svg>Number one</h3>
      <p class="point__text">What we need is a template (or master) which can be varied by ourselves from case to case. Most of our cases are colorful and it's important to transport the passion of</p>
    </article>
    <article class="point">
      <h3 class="point__head"><svg width="26" height="22" viewBox="0 0 26 22"><path d="M1 1h24v15H9l-5 5v-5H1z" fill="#fff"/><path d="M6 13V4l7 6 7-6v9" fill="none" stroke="var(--green)" stroke-width="2.4"/></svg>Number one</h3>
      <p class="point__text">What we need is a template (or master) which can be varied by ourselves from case to case. Most of our cases are colorful and it's important to transport the passion of</p>
    </article>
  </div>
  <blockquote class="testimonial">
    <p class="testimonial__title">Testimonials comes here</p>
    <p class="testimonial__quote">“ What we need is a template (or master) which can be varied by ourselves from case to case. Most of our cases are colorful and it's important to transport the passion of”.</p>
    <p class="testimonial__name">Followed by name of the person</p>
  </blockquote>
  <footer class="slide__footer"><div class="footer__bar">
    <div class="footer__nav"><span></span><span></span></div>
    <div class="wordmark"><span class="wordmark__dot"></span>brenthollow</div>
    <span class="footer__copy">© Copy right to brenthollow wisdom &amp; knowledge</span>
  </div></footer>
</section>

<section class="slide slide--team">
  <h2 class="slide__title">Our Team members</h2>
  <p class="slide__subtitle">Your sub title here</p>
  <svg class="team__band" width="514" height="156" viewBox="0 0 514 156">
    <defs>
      <linearGradient id="photoTone" x1="0" y1="0" x2="0" y2="1"><stop offset="0" stop-color="#cfcfcf"/><stop offset="1" stop-color="#9a9a9a"/></linearGradient>
    </defs>
    <rect x="0" y="0" width="514" height="78" fill="var(--green)"/>
    <rect x="0" y="78" width="514" height="78" fill="#2f2f2f"/>
    <g fill="#ececec">
      <polygon points="236,0 262,0 244,78 218,0"/>
      <polygon points="342,0 368,0 350,78 324,78"/>
      <polygon points="448,0 474,0 456,78 430,78"/>
      <polygon points="218,0 236,0 218,78 200,78"/>
    </g>
    <rect x="174" y="6" width="62" height="72" fill="url(#photoTone)" role="img" aria-label="Portrait photo of team member"/>
    <rect x="280" y="6" width="62" height="72" fill="url(#photoTone)" role="img" aria-label="Portrait photo of team member"/>
    <rect x="386" y="6" width="62" height="72" fill="url(#photoTone)" role="img" aria-label="Portrait photo of team member"/>
    <rect x="208" y="84" width="62" height="72" fill="url(#photoTone)" role="img" aria-label="Portrait photo of Kaori Menda"/>
    <rect x="322" y="84" width="62" height="72" fill="url(#photoTone)" role="img" aria-label="Portrait photo of Takeshi Ryo"/>
    <rect x="428" y="84" width="62" height="72" fill="url(#photoTone)" role="img" aria-label="Portrait photo of Naomi Seto"/>
  </svg>
  <div class="wordmark team__logo"><span class="wordmark__dot"></span>brenthollow</div>
  <p class="member member--a"><span class="member__name">KAORI<br>MENDA</span><span class="member__role">Partner</span></p>
  <p class="member member--b"><span class="member__name">TAKESHI<br>RYO</span><span class="member__role">Senior<br>consultant</span></p>
  <p class="member member--c"><span class="member__name">NAOMI<br>SETO</span><span class="member__role">Partner</span></p>
  <footer class="slide__footer"><div class="footer__bar">
    <div class="footer__nav"><span></span><span></span><span></span></div>
    <div class="wordmark"><span class="wordmark__dot"></span>brenthollow</div>
    <span class="footer__copy">© Copy right to brenthollow wisdom &amp; knowledge</span>
  </div></footer>
</section>

</body>
</html>
```